Labeling for Organic Food

we need a label design for

1. Organic Red Rice
2. Organic wild honey

it is going to be the same design in different dimensions.

1. Organic Red Rice
Dimension 1 28*18.5cm
Dimension 2 13.5*8cm

2. Organic Honey
12*6cm
Updates

There is an update in the brief about using the Bhutanese color scheme. Please check it out.

Target Market(s)

people with the concern of health and the environment.

Requirements
Must have
• 1. our logo
• 2. All the info
• 3. A natural feel
• 4. I would prefer minimalistic style
• 5. Please include Bhutanese national colours as attached.

```html
<!DOCTYPE html>
<html lang="en">
<head>
<meta charset="utf-8">
<title>Organic Wild Honey Label</title>
<link href="https://fonts.googleapis.com/css2?family=Arimo:ital,wght@0,400;0,700;1,400&family=Noto+Sans+SC:wght@700&display=swap" rel="stylesheet">
<style>
  :root {
    --honey-light: #fffbe8;
    --honey-mid: #fdefb8;
    --honey-deep: #f9dc86;
    --brown: #5a3418;
    --brown-box: #5b3a1f;
    --ink: #2f2418;
    --white: #ffffff;
  }
  * { margin: 0; padding: 0; box-sizing: border-box; }
  html, body {
    width: 1200px;
    height: 600px;
    overflow: hidden;
    background: var(--white);
  }
  .label {
    position: relative;
    width: 1200px;
    height: 600px;
    overflow: hidden;
    font-family: "Arimo", Arial, sans-serif;
    color: var(--ink);
  }
  .label__backdrop {
    position: absolute;
    inset: 0;
    background:
      radial-gradient(ellipse 55% 60% at 50% 45%, var(--honey-light) 0%, var(--honey-mid) 60%, var(--honey-deep) 100%);
  }
  .product-title {
    position: absolute;
    left: 0;
    width: 1228px;
    text-align: center;
    color: var(--brown);
    font-weight: 700;
    text-shadow:
      3px 0 0 var(--white), -3px 0 0 var(--white), 0 3px 0 var(--white), 0 -3px 0 var(--white),
      2px 2px 0 var(--white), -2px -2px 0 var(--white), 2px -2px 0 var(--white), -2px 2px 0 var(--white);
  }
  .product-title--en {
    top: 76px;
    font-size: 49px;
    line-height: 1.1;
  }
  .product-title--zh {
    top: 140px;
    font-family: "Noto Sans SC", sans-serif;
    font-size: 52px;
    line-height: 1.1;
    letter-spacing: 2px;
  }
  .description {
    position: absolute;
    top: 226px;
    left: 332px;
    width: 564px;
    text-align: center;
    font-size: 21.5px;
    line-height: 30px;
    color: var(--ink);
  }
  .info-line {
    position: absolute;
    left: 332px;
    width: 564px;
    text-align: center;
    font-size: 18px;
    font-weight: 700;
    color: var(--brown);
  }
  .info-line--ingredients { top: 462px; }
  .info-line--storage { top: 498px; }
  .distributor {
    position: absolute;
    left: 50px;
    top: 412px;
  }
  .distributor__caption {
    font-style: italic;
    font-size: 19px;
    color: var(--ink);
  }
  .distributor__brand {
    display: flex;
    align-items: center;
    gap: 8px;
    margin-top: 14px;
    font-size: 40px;
    font-weight: 700;
    color: var(--ink);
    line-height: 1;
  }
  .distributor__mark {
    width: 14px;
    height: 14px;
    border-radius: 50%;
    background: var(--ink);
  }
  .distributor__address {
    margin-top: 12px;
    font-size: 20px;
    line-height: 25px;
    color: var(--ink);
  }
  .spec-box {
    position: absolute;
    left: 925px;
    top: 460px;
    width: 240px;
    height: 100px;
    background: var(--brown-box);
    color: var(--white);
    text-align: center;
    padding-top: 13px;
    font-size: 20px;
    line-height: 25px;
  }
  .spec-box__strong { font-weight: 700; }
</style>
</head>
<body>
  <main class="label">
    <div class="label__backdrop" role="img" aria-label="Soft golden honeycomb hexagon pattern background"></div>

    <h1 class="product-title product-title--en">Organic Wild Honey</h1>
    <p class="product-title product-title--zh" lang="zh">有机野生蜂蜜</p>

    <p class="description">
      Organic Wild Honey is freshly collected from the remote unpolluted lands of the Himalayans in Bhutan. The bees are not fed sugar and antibiotics and the honey is free from chemical preservatives, coloring and additives. The wild honey is not heat treated and unprocessed to retain the optimum level of nutritional value and enzymes.
    </p>

    <p class="info-line info-line--ingredients">Ingredients: Organic Bhutanese, Wild Honey</p>
    <p class="info-line info-line--storage">Store in a cool and dry place</p>

    <section class="distributor">
      <p class="distributor__caption">Distributed by</p>
      <p class="distributor__brand">Verdaleaf<span class="distributor__mark"></span></p>
      <p class="distributor__address">27 Willow Bank Road<br>Singapore 600123</p>
    </section>

    <aside class="spec-box">
      <p class="spec-box__strong">Net Weight 250ml</p>
      <p class="spec-box__strong">Best before 31/12/19</p>
      <p>Product of Bhutan</p>
    </aside>
  </main>
</body>
</html>
```